Fundrally Slides

I need a graphic designer go through the attached power point presentation (4 slides) and make it look clean, modern, and branded.

The four slides are currently displayed as jpegs on the Fundrally viewing page below -
Here is the Fundrally preview link:: https://www.fundrally.example/projects/4826153907/5390284716?token=3c7a91f2
Updates

Project Deadline Extended

Industry/Entity Type

Graphic Designer

Requirements
Must have
• Simple, clean same color scheme as logo

```html
<!DOCTYPE html>
<html lang="en">
<head>
<meta charset="utf-8">
<title>Stapra Slides</title>
<link rel="stylesheet" href="https://fonts.googleapis.com/css2?family=PT+Sans:wght@400;700&display=swap">
<style>
:root{
  --stage:#161616;
  --paper:#ffffff;
  --mist:#e9eaec;
  --silver:#cfd1d4;
  --royal:#1f3fc4;
  --royal-deep:#12309a;
  --navy:#142a6e;
  --sky:#1c74c9;
  --ink:#3a3a3a;
  --ink-soft:#555;
  --grey-title:#7a7a7a;
}
*{box-sizing:border-box;margin:0;padding:0}
html,body{width:1200px;height:1000px;overflow:hidden;background:var(--stage)}
body{position:relative;font-family:"PT Sans",Arial,sans-serif;color:var(--ink)}
.slide{position:absolute;background:var(--paper);overflow:hidden}
.slide svg.backdrop{position:absolute;inset:0}
.cover{left:347px;top:72px;width:506px;height:383px}
.overview{left:78px;top:513px;width:509px;height:384px}
.facts{left:616px;top:513px;width:509px;height:384px}

.brand-name{font-weight:700;color:var(--navy);display:flex;align-items:center;gap:6px;letter-spacing:1px;white-space:nowrap}
.brand-name .mark{width:10px;height:10px;background:var(--royal);display:inline-block}
.cover .brand-name{position:absolute;left:74px;top:150px;font-size:46px}
.cover .brand-name .mark{width:20px;height:20px}
.cover .contact{position:absolute;left:356px;top:310px;text-align:center;font-size:10px;line-height:12px;color:var(--navy);white-space:nowrap}
.contact strong{font-weight:700;font-size:11px}

.slide-title{position:absolute;left:14px;top:20px;font-size:23px;font-weight:400;color:var(--grey-title);letter-spacing:-.3px}
.slide-title b{font-weight:700;color:var(--navy)}
.body-copy{position:absolute;left:15px;top:60px;width:302px;font-size:8.3px;line-height:10.6px;text-align:justify;color:var(--ink-soft)}
.body-copy p{margin-bottom:9px}

.figure-label{position:absolute;left:342px;width:120px;text-align:center;font-size:9px;color:var(--sky)}
.figure-art{position:absolute;left:342px;width:120px;border:1px solid #999}
.fig-1a{top:72px;height:40px;background:linear-gradient(90deg,#e6e6e6 50%,#d8b7a4 50%)}
.fig-2b{top:129px;height:124px;background:linear-gradient(180deg,#eeeeee 50%,#c79a73 50%)}

.footer-brand{position:absolute;right:8px;top:336px;display:flex;align-items:center;gap:6px}
.footer-brand .brand-name{font-size:18px}
.footer-brand .rule{width:1px;height:34px;background:#888}
.footer-brand .contact{font-size:7px;line-height:8.6px;color:#333;white-space:nowrap}
.footer-brand .contact strong{font-size:7.5px}

.subtitle{position:absolute;left:20px;top:49px;font-size:10.5px;font-weight:700;color:var(--sky)}
.fact-list{position:absolute;left:18px;top:72px;width:262px;list-style:none;font-size:8.4px;line-height:12.4px;color:var(--ink-soft)}
.fact-list li{padding-left:7px;text-indent:-7px}
.fact-list li::before{content:"• "}
.chart-card{position:absolute;left:296px;top:75px;width:186px;height:172px;border:1.5px solid #333;background:#fff}
</style>
</head>
<body>

<section class="slide cover">
  <svg class="backdrop" width="506" height="383" viewBox="0 0 506 383">
    <polygon points="0,0 180,0 385,172 180,383 0,383" fill="var(--mist)" opacity=".6"/>
    <polygon points="40,0 120,0 330,172 120,383 60,383 280,172" fill="var(--silver)" opacity=".7"/>
    <polygon points="380,0 506,0 506,40" fill="var(--silver)" opacity=".6"/>
    <polygon points="430,383 506,383 506,300" fill="var(--silver)" opacity=".6"/>
    <polygon points="178,0 270,0 388,172 212,383 118,383 340,172" fill="var(--royal)"/>
    <polygon points="270,0 506,0 506,78 388,172" fill="var(--royal)"/>
    <polygon points="388,172 506,230 506,370" fill="var(--royal-deep)"/>
  </svg>
  <div class="brand-name"><span class="mark"></span>STAPRA</div>
  <div class="contact"><strong>VELL MEDICA, LLC</strong><br>1250 HARBOR AVE SUITE 410<br>BAYVIEW, FL 33000<br>305.555.0148</div>
</section>

<section class="slide overview">
  <svg class="backdrop" width="509" height="384" viewBox="0 0 509 384">
    <polygon points="0,300 509,240 509,286 0,384" fill="var(--royal)" opacity=".75"/>
    <polygon points="0,290 280,384 200,384 0,330" fill="var(--navy)" opacity=".8"/>
    <polygon points="0,340 180,384 0,384" fill="var(--royal-deep)" opacity=".6"/>
  </svg>
  <h1 class="slide-title">General <b>Overview</b></h1>
  <div class="body-copy">
    <p>The Stapra is the first device to successfully automate the hygienic removal of surgical staples.</p>
    <p>Problem: Surgical wounds and lacerations are closed in multiple fashions and often surgical staples are used to reapproximate the edges. Upon wound healing, the current method of removal of the staple is suboptimal and potentially dangerous. The process requires the doctor or nurse to deform the staple from a "U" shape to a "W" shape (Fig 1A). Each deformation requires focus on the wound, only to be diverted for subsequent disposal into a container or receptacle away from the wound, and then subsequent refocus on the site.</p>
    <p>This process is inefficient and unsanitary. The removal of the staple creates a "sharp", which can transmit disease and/ or injury, through inadvertent puncture of a Healthcare or Sanitation worker.</p>
    <p>Solution: The Stapra deforms the staple in the same manner as the aforementioned; however, it then automatically places the bio hazardous removed staple into a self contained isolated compartment within the device for safe and hygienic disposable at the completion of the removal procedure (Fig 2B).</p>
  </div>
  <div class="figure-label" style="top:60px">Figure 1A</div>
  <div class="figure-art fig-1a" role="img" aria-label="Diagram of a staple deformed from U to W shape beside a photo of staple removal on skin"></div>
  <div class="figure-label" style="top:117px">Figure 2B</div>
  <div class="figure-art fig-2b" role="img" aria-label="Line drawings of the remover mechanism above photos of the device held in a gloved hand"></div>
  <div class="footer-brand">
    <div class="brand-name"><span class="mark"></span>STAPRA</div>
    <span class="rule"></span>
    <div class="contact"><strong>VELL MEDICA, LLC</strong><br>1250 HARBOR AVE SUITE 410<br>BAYVIEW, FL 33000<br>305.555.0148</div>
  </div>
</section>

<section class="slide facts">
  <svg class="backdrop" width="509" height="384" viewBox="0 0 509 384">
    <polygon points="300,0 509,0 509,70" fill="var(--mist)" opacity=".7"/>
    <polygon points="0,300 509,240 509,286 0,384" fill="var(--royal)" opacity=".75"/>
    <polygon points="0,290 280,384 200,384 0,330" fill="var(--navy)" opacity=".8"/>
    <polygon points="0,340 180,384 0,384" fill="var(--royal-deep)" opacity=".6"/>
  </svg>
  <h1 class="slide-title" style="left:18px">The <b>Facts</b></h1>
  <div class="subtitle">National Health Safety Agency Statistics</div>
  <ul class="fact-list">
    <li>385,000 percutaneous injuries occur in US hospitals annually.</li>
    <li>It's documented that half or more injuries go unreported.</li>
    <li>Those injured include: nursing staff, laboratory staff, physicians, housekeepers, and other health care workers.</li>
    <li>National Health Safety Agency defines a "Sharps Injury" as a penetrating stab wound from a needle, scalpel, or other sharp object that may result in exposure to blood or other body fluids.</li>
    <li>A report from the Sharps Injury Tracking Network (SITNet) found that nearly half of all sharps injuries occurred during use of the sharp, and of the nearly 40% of needle injuries which involved a safety designed needle, the majority occurred before activating the safety device.</li>
    <li>24% of injuries caused by a suture needle.</li>
    <li>22% of Sharps injuries are caused by surgical staples or like sharps.</li>
  </ul>
  <svg class="chart-card" viewBox="0 0 186 172" font-family="PT Sans, Arial, sans-serif">
    <rect x="0" y="0" width="186" height="14" fill="#f2f2f2"/>
    <text x="4" y="10" font-size="6.5" font-weight="700" fill="#222">How do sharps injuries occur?</text>
    <text font-size="3.8" fill="#444">
      <tspan x="4" y="20">Besides device use, injuries also link to certain work practices that</tspan>
      <tspan x="4" y="25">raise exposure risk. These practices include:</tspan>
      <tspan x="6" y="31">• Disposal-related activities (13%)</tspan>
      <tspan x="6" y="36">• Activities after use and prior to disposal (30%)</tspan>
      <tspan x="6" y="41">• Recapping a used needle (5%)</tspan>
    </text>
    <g transform="translate(84,96)">
      <path d="M0,0 L0,-38 A38,38 0 0 1 34,17 Z" fill="#c0504d"/>
      <path d="M0,0 L34,17 A38,38 0 0 1 22,31 Z" fill="#8064a2"/>
      <path d="M0,0 L22,31 A38,38 0 0 1 15,35 Z" fill="#9bbb59"/>
      <path d="M0,0 L15,35 A38,38 0 0 1 -4,38 Z" fill="#4bacc6"/>
      <path d="M0,0 L-4,38 A38,38 0 0 1 0,-38 Z" fill="#4f81bd"/>
    </g>
    <text font-size="3.8" fill="#333">
      <tspan x="12" y="70">During use 41%</tspan>
      <tspan x="126" y="74">After use before disposal 30%</tspan>
      <tspan x="126" y="104">Disposal related 13%</tspan>
      <tspan x="126" y="118">Recapping 5%</tspan>
      <tspan x="110" y="134">Other 11%</tspan>
    </text>
    <rect x="4" y="120" width="42" height="37" fill="var(--navy)"/>
    <text x="4" y="164" font-size="3.8" fill="#333">Figure 1: Activities linked to percutaneous injuries in US hospitals, by % total.</text>
  </svg>
  <div class="footer-brand">
    <div class="brand-name"><span class="mark"></span>STAPRA</div>
    <span class="rule"></span>
    <div class="contact"><strong>VELL MEDICA, LLC</strong><br>1250 HARBOR AVE SUITE 410<br>BAYVIEW, FL 33000<br>305.555.0148</div>
  </div>
</section>

</body>
</html>
```